App Design

This is a 'video player' app - will be used to stream video files and watch them on a device. Need 3/4 skins for user customization.
Design will need to be versatile - used on: Veltrax4/4S/5 and zorBex2/3
Require an app design that shows the required functionality described by us, allows ease to navigate and visually creates a unique user experience.
App must have following pages: (refer to attached pages)
1. Search Page
2. Results Page
3. Video Page
4. End Page
3-4 skins for user preference
important: if you are interested please submit designs by tomorrow night - we will be picking from submitted designs - will make revisions and finalize the design within 4-5 days.
timing is crucial- please only submit if you can commit to timeline and design requirements. There will be refinements required.
Please see the attached update.
Additional reference files have been added to help in your efforts.
We have added a sample design that may help with your submissions. Please see brief
Project Deadline Extended
Project Deadline Extended
Project Deadline Extended
Target Market(s)
early adapters for technology / veltrax, tablet, quillon users
Requirements
Should not have
- should not be generic design

```html
<!DOCTYPE html>
<html lang="en">
<head>
<meta charset="utf-8">
<title>Vantic Loop – Settings</title>
<link rel="stylesheet" href="https://fonts.googleapis.com/css2?family=Open+Sans:wght@400;700;800&display=swap">
<style>
  :root {
    --bg-top: #2c1233;
    --bg-mid: #4e1d5a;
    --bg-bottom: #2a1131;
    --brand: #b54de6;
    --toggle-on: #c300f2;
    --toggle-off-light: #f4f4f4;
    --toggle-off-dark: #a9a9a9;
    --text: #ffffff;
    --panel-line: #e6dcea;
    --tab-border: #8d2ea6;
    --tab-top: #3a3a3a;
    --tab-bottom: #161616;
    --icon-light: #c9dcef;
    --icon-mid: #8fb1d1;
    --icon-dark: #2d2d2d;
  }
  * { box-sizing: border-box; margin: 0; padding: 0; }
  html, body { width: 799px; height: 1200px; overflow: hidden; }
  body {
    position: relative;
    font-family: "Open Sans", Arial, sans-serif;
    color: var(--text);
    background: linear-gradient(180deg, var(--bg-top) 0%, var(--bg-mid) 55%, var(--bg-bottom) 100%);
  }
  .brand { position: absolute; left: 34px; top: 30px; display: flex; align-items: center; gap: 28px; }
  .brand-mark { width: 108px; height: 107px; background: var(--brand); }
  .brand-name { font-size: 28px; font-weight: 400; color: var(--brand); margin-top: 10px; }

  .toggle { position: absolute; display: flex; width: 120px; height: 38px; }
  .toggle-on { width: 50%; background: var(--toggle-on); border: 3px solid #000; }
  .toggle-off { width: 50%; background: linear-gradient(90deg, var(--toggle-off-light), var(--toggle-off-dark)); border: 1px solid #555; }
  .theme-toggle { left: 645px; top: 41px; }

  .heading { position: absolute; left: 125px; font-weight: 700; line-height: 1; }
  .heading-settings { top: 192px; font-size: 40px; }
  .heading-features { top: 270px; font-size: 39px; }

  .features-panel { position: absolute; left: 110px; top: 321px; width: 575px; height: 341px; border: 1px solid var(--panel-line); }
  .feature-row { position: absolute; left: 35px; }
  .feature-row .switch-label { position: absolute; left: 20px; top: -31px; font-size: 20px; font-weight: 700; white-space: nowrap; }
  .feature-row .toggle { position: relative; }
  .feature-name { position: absolute; left: 170px; top: -8px; font-size: 39px; font-weight: 700; white-space: nowrap; }

  .menu-list { position: absolute; left: 125px; top: 696px; list-style: none; }
  .menu-list li { font-size: 30px; font-weight: 700; height: 60.5px; line-height: 40px; }

  .tab-bar { position: absolute; left: 20px; top: 996px; width: 761px; height: 184px; }
  .tab { position: absolute; top: 0; width: 185px; height: 184px; border: 4px solid var(--tab-border);
         background: linear-gradient(180deg, var(--tab-top), var(--tab-bottom)); overflow: hidden; }
  .tab svg, .tab .icon-fill { position: absolute; }
  .tab-label { position: absolute; left: 0; right: 0; bottom: 4px; text-align: center; font-size: 27px; font-weight: 400; }
  .tab-favourites { left: 0; }
  .tab-trending { left: 192px; }
  .tab-search { left: 383px; }
  .tab-settings { left: 576px; }
  .icon-fill { left: 22px; top: 8px; width: 135px; height: 135px; border-radius: 50%;
               border: 3px solid #5f6f80;
               background: radial-gradient(circle at 40% 35%, #d6e4f2, #9ab6d2); }
</style>
</head>
<body>
  <header class="brand">
    <div class="brand-mark"></div>
    <span class="brand-name">Vantic Loop</span>
  </header>
  <div class="toggle theme-toggle"><span class="toggle-on"></span><span class="toggle-off"></span></div>

  <h1 class="heading heading-settings">Settings</h1>
  <h2 class="heading heading-features">Features</h2>

  <section class="features-panel">
    <div class="feature-row" style="top:45px">
      <span class="switch-label">ON/OFF</span>
      <div class="toggle"><span class="toggle-on"></span><span class="toggle-off"></span></div>
      <span class="feature-name">Features 1</span>
    </div>
    <div class="feature-row" style="top:156px">
      <span class="switch-label">ON/OFF</span>
      <div class="toggle"><span class="toggle-on"></span><span class="toggle-off"></span></div>
      <span class="feature-name">Features 2</span>
    </div>
    <div class="feature-row" style="top:265px">
      <span class="switch-label">ON/OFF</span>
      <div class="toggle"><span class="toggle-on"></span><span class="toggle-off"></span></div>
      <span class="feature-name">Features 3</span>
    </div>
  </section>

  <ul class="menu-list">
    <li>Help</li>
    <li>About</li>
    <li>Feedback</li>
    <li>Privacy</li>
    <li>Term of Use</li>
  </ul>

  <nav class="tab-bar">
    <div class="tab tab-favourites">
      <div class="icon-fill" role="img" aria-label="Favourites emblem: round pale blue smiling character"></div>
      <span class="tab-label">Favourites</span>
    </div>
    <div class="tab tab-trending">
      <svg width="177" height="140" viewBox="0 0 177 140" aria-hidden="true">
        <circle cx="40" cy="45" r="20" fill="var(--icon-mid)" stroke="var(--icon-dark)" stroke-width="3"/>
        <circle cx="137" cy="45" r="20" fill="var(--icon-mid)" stroke="var(--icon-dark)" stroke-width="3"/>
        <path d="M8 112 Q8 72 40 72 Q72 72 72 112 Z" fill="var(--icon-mid)" stroke="var(--icon-dark)" stroke-width="3"/>
        <path d="M105 112 Q105 72 137 72 Q169 72 169 112 Z" fill="var(--icon-mid)" stroke="var(--icon-dark)" stroke-width="3"/>
        <circle cx="88" cy="40" r="24" fill="var(--icon-light)" stroke="var(--icon-dark)" stroke-width="3"/>
        <path d="M46 122 Q46 72 88 72 Q130 72 130 122 Z" fill="var(--icon-light)" stroke="var(--icon-dark)" stroke-width="3"/>
      </svg>
      <span class="tab-label">Trending</span>
    </div>
    <div class="tab tab-search">
      <svg width="177" height="140" viewBox="0 0 177 140" aria-hidden="true">
        <line x1="92" y1="80" x2="150" y2="130" stroke="#9a9a9a" stroke-width="18" stroke-linecap="round"/>
        <circle cx="58" cy="46" r="44" fill="var(--icon-light)" stroke="#b5b5b5" stroke-width="10"/>
      </svg>
      <span class="tab-label">Search</span>
    </div>
    <div class="tab tab-settings">
      <svg width="177" height="140" viewBox="0 0 177 140" aria-hidden="true">
        <g fill="var(--icon-mid)" stroke="var(--icon-dark)" stroke-width="2">
          <circle cx="42" cy="34" r="22" stroke-dasharray="8 4" stroke-width="12"/>
          <circle cx="42" cy="34" r="8" fill="var(--icon-dark)"/>
          <circle cx="112" cy="84" r="36" stroke-dasharray="11 6" stroke-width="18"/>
          <circle cx="112" cy="84" r="12" fill="var(--icon-dark)"/>
        </g>
      </svg>
      <span class="tab-label">Settings</span>
    </div>
  </nav>
</body>
</html>
```